Forest Consultant/Timber Buyer needs a clean business card

We are a forestry consulting and timber buying company. We meet with private landowners and assist them with timber management and timber harvesting. We would like a professional business card, please no clip art. logo is blue and white but would like to see a gray,silver, or some other color incorporated. Would like basic contact info. Would like to the layout to be creative and sleek but masculine.

Target Market(s)

private landowners

Industry/Entity Type

Business

Contact Information for Business Card

name,position, cell number, office number, email, website. This might be to cluttered. Basic contact info is what we are looking for.

Contact info can all be on one side with logo on the other.

Font styles to use
Serif
Sans Serif

Colors
0255a3
ffffff
aaaaaa

Requirements
Must have
• We just want it professional.
Nice to have
• Creative layout.
Should not have
• please no clip art of log trucks etc.

```html
<!DOCTYPE html>
<html lang="en">
<head>
<meta charset="utf-8">
<title>Ridgeline Land &amp; Timber – Business Card</title>
<link rel="stylesheet" href="https://fonts.googleapis.com/css2?family=Open+Sans:wght@400;600;700&display=swap">
<style>
  :root {
    --backdrop: #3a3735;
    --card-dark: #2a2a2c;
    --card-back: #262628;
    --brand-blue: #1f6fd0;
    --band-blue: #1a64c2;
    --edge-grey: #8d8d8f;
    --silver: #d6d6d8;
    --ink-dark: #1b2533;
    --white: #ffffff;
  }
  html, body {
    margin: 0;
    padding: 0;
    width: 1200px;
    height: 716px;
    overflow: hidden;
    background: var(--backdrop);
    font-family: "Open Sans", Arial, sans-serif;
  }
  .canvas {
    position: relative;
    width: 1200px;
    height: 716px;
  }
  .card {
    position: absolute;
    top: 203px;
    width: 540px;
    height: 310px;
    border-radius: 3px;
    overflow: hidden;
    box-shadow: 0 10px 30px rgba(0,0,0,.45);
  }
  .card-front { left: 45px; background: var(--card-dark); }
  .card-back { left: 615px; background: var(--card-back); }

  .front-band { position: absolute; inset: 0; }

  .front-brand {
    position: absolute;
    top: 26px;
    left: 30px;
    display: flex;
    align-items: center;
    gap: 10px;
    color: var(--brand-blue);
    font-weight: 700;
    font-size: 20px;
    letter-spacing: 1px;
    text-transform: uppercase;
  }
  .brand-dot {
    width: 22px;
    height: 22px;
    border-radius: 50%;
    background: var(--brand-blue);
  }

  .contact-list {
    position: absolute;
    left: 30px;
    top: 150px;
    margin: 0;
    padding: 0;
    list-style: none;
    color: var(--white);
    font-size: 12px;
    line-height: 21px;
  }
  .contact-list li { display: flex; align-items: center; gap: 8px; }
  .contact-list svg { width: 12px; height: 12px; }

  .person {
    position: absolute;
    left: 250px;
    top: 138px;
  }
  .person-name {
    margin: 0;
    color: var(--ink-dark);
    font-size: 19px;
    font-weight: 600;
    letter-spacing: .5px;
  }
  .person-role {
    margin: 4px 0 0;
    color: var(--white);
    font-size: 10px;
    font-weight: 600;
    letter-spacing: .3px;
  }

  .address {
    position: absolute;
    left: 300px;
    top: 222px;
    color: var(--white);
    font-size: 11.5px;
    line-height: 18px;
    font-style: normal;
    text-transform: uppercase;
  }
  .address .web { text-transform: none; }

  .back-brand {
    position: absolute;
    inset: 0;
    display: flex;
    align-items: center;
    justify-content: center;
    gap: 16px;
    color: var(--silver);
    font-weight: 700;
    font-size: 30px;
    letter-spacing: 2px;
    text-transform: uppercase;
  }
  .back-brand .brand-dot {
    width: 30px;
    height: 30px;
    background: var(--silver);
  }
</style>
</head>
<body>
<main class="canvas">
  <section class="card card-front" aria-label="Business card front">
    <svg class="front-band" viewBox="0 0 540 310" width="540" height="310" aria-hidden="true">
      <path d="M0,108 Q250,40 540,150 L540,310 L0,310 Z" fill="var(--band-blue)"/>
      <path d="M0,108 Q250,40 540,150" fill="none" stroke="var(--edge-grey)" stroke-width="5"/>
    </svg>

    <div class="front-brand">
      <span class="brand-dot"></span>
      <span>Ridgeline Land &amp; Timber</span>
    </div>

    <ul class="contact-list">
      <li>
        <svg viewBox="0 0 12 12" aria-hidden="true"><rect x="0" y="0" width="12" height="12" rx="2" fill="#16407a"/><path d="M3,2.5 L5,2.5 L5.5,4.5 L4.5,5.3 Q5.5,7 7,7.8 L7.8,6.8 L9.5,7.3 L9.5,9.3 Q5,9.5 2.7,3.2 Z" fill="#fff"/></svg>
        0400 123 456
      </li>
      <li>
        <svg viewBox="0 0 12 12" aria-hidden="true"><rect x="0" y="0" width="12" height="12" rx="2" fill="#16407a"/><rect x="3.5" y="2" width="5" height="8" rx="1" fill="#fff"/></svg>
        0400 123 456
      </li>
      <li>
        <svg viewBox="0 0 12 12" aria-hidden="true"><rect x="0" y="0" width="12" height="12" rx="2" fill="#16407a"/><rect x="2.5" y="3.5" width="7" height="5" fill="none" stroke="#fff"/><path d="M2.5,3.5 L6,6.3 L9.5,3.5" fill="none" stroke="#fff"/></svg>
        dharlow@pinecrestlodge.com.au
      </li>
    </ul>

    <div class="person">
      <p class="person-name">DALE HARLOW</p>
      <p class="person-role">FINANCE MANAGER</p>
    </div>

    <address class="address">
      BCOM, 27 Marlow Way<br>
      Pine Crest, QLD 4000.<br>
      <span class="web">www.pinecrestlodge.com.au</span>
    </address>
  </section>

  <section class="card card-back" aria-label="Business card back">
    <div class="back-brand">
      <span class="brand-dot"></span>
      <span>Ridgeline Land &amp; Timber</span>
    </div>
  </section>
</main>
</body>
</html>
```